My Web Development Portfolio site

I'm a web developer and I need a web design that can showcase my web development portfolio. I like most of the websites from this link: http://www.mintquarry.example/galleries/samples-493051. My ideal design should be modern, clean and fun. I will let the designer decided the color theme for the website.

Target Market(s)

Potential Employers.

Number of Pages Required

1 page

Requirements
Must have
• - Menu bar that includes at least: About Me, Blog, Contact, Project/Work
• - Excellent color theme
• - Use the logo I provided (see attachment)
Nice to have
• - Some animation
• - Fun yet modern design

```html
<!DOCTYPE html>
<html lang="en">
<head>
<meta charset="utf-8">
<title>pixelharbor — Web Developer Portfolio</title>
<link href="https://fonts.googleapis.com/css2?family=Open+Sans:ital,wght@0,400;0,600;0,700;1,400&family=Oswald:wght@400;500&display=swap" rel="stylesheet">
<style>
:root{
  --sky:#6cb6ee;
  --sky-light:#a6d6f7;
  --paper:#f2f2f2;
  --ink:#333333;
  --accent-blue:#1a7fd6;
  --coral:#e8634b;
  --coral-light:#ee7a62;
  --sand:#ecd8ae;
  --sand-light:#f2e2bf;
  --sand-field:#fbf5e6;
  --caramel:#d4772e;
  --footer:#333333;
  --white:#ffffff;
}
*{box-sizing:border-box;margin:0;padding:0}
html,body{width:1200px;height:2679px;overflow:hidden}
body{position:relative;font-family:"Open Sans",Arial,sans-serif;color:var(--ink);background:var(--white)}
.abs{position:absolute}
.display{font-family:"Oswald","Arial Narrow",sans-serif;text-transform:uppercase;letter-spacing:.14em;font-weight:500}

/* hero */
.hero{left:0;top:0;width:1200px;height:625px;background:var(--sky);overflow:hidden}
.topbar{left:0;top:0;width:1200px;height:134px;background:rgba(40,110,180,.08)}
.brand{left:100px;top:86px;font-size:30px;line-height:1;font-weight:400;color:var(--white);letter-spacing:.02em}
.nav a{position:absolute;top:0;font-size:16px;font-weight:700;color:#111;text-decoration:none;white-space:nowrap}
.nav{left:437px;top:98px}
.phone{left:984px;top:96px;display:flex;align-items:center;gap:8px;color:var(--white);font-size:20px;font-weight:600}
.hero-kicker{left:75px;top:294px;font-size:17px;color:var(--white);letter-spacing:.24em}
.hero-title{left:75px;top:320px;font-size:45px;line-height:1;color:var(--white);letter-spacing:.1em}
.hero-title2{left:75px;top:370px;font-size:28px;color:var(--white);letter-spacing:.14em}
.hero-copy{left:75px;top:433px;width:345px;font-size:13.5px;line-height:1.65;color:var(--white)}
.hero-art{left:607px;top:268px;width:375px;height:357px;border-radius:8px 8px 0 0;background:linear-gradient(180deg,rgba(255,255,255,0) 0%,rgba(244,160,90,.55) 70%,rgba(180,110,60,.7) 100%)}

/* services */
.services{left:0;top:625px;width:1200px;height:657px;background:var(--paper)}
.section-title{font-size:36px;font-weight:400;color:#444;letter-spacing:.16em;line-height:1}
.section-sub{font-family:"Oswald","Arial Narrow",sans-serif;font-size:12px;letter-spacing:.22em;text-transform:uppercase;color:#333}
.services-art{left:71px;top:241px;width:440px;height:232px;border-radius:6px;background:linear-gradient(160deg,#5fa3e8 0%,#dfe6ef 55%,#e9e9e9 100%)}
.service{width:236px}
.service h3{font-family:"Oswald","Arial Narrow",sans-serif;font-weight:500;font-size:22px;letter-spacing:.14em;text-transform:uppercase;color:var(--accent-blue);line-height:1;white-space:nowrap}
.service h4{font-family:"Oswald","Arial Narrow",sans-serif;font-weight:500;font-size:12px;letter-spacing:.3em;color:var(--accent-blue);text-transform:uppercase;margin-top:4px}
.service p{margin-top:22px;font-size:13px;line-height:1.85;color:#444}
.btn{display:inline-block;border:1.5px solid #555;font-family:"Oswald","Arial Narrow",sans-serif;text-transform:uppercase;letter-spacing:.3em;font-size:14px;color:#333;text-align:center;line-height:30px;text-decoration:none}

/* work */
.work{left:0;top:1282px;width:1200px;height:358px}
.tile{width:268px;height:179px}
.work-panel{left:804px;top:0;width:396px;height:358px;background:var(--coral);overflow:hidden}
.work-panel h2{position:absolute;left:0;width:100%;top:36px;text-align:center;font-size:36px;font-weight:400;line-height:1;color:var(--white)}
.work-panel h3{position:absolute;left:0;width:100%;top:84px;text-align:center;font-family:"Oswald","Arial Narrow",sans-serif;font-size:12px;font-weight:500;letter-spacing:.22em;color:var(--white)}
.work-panel p{position:absolute;left:78px;width:240px;top:118px;text-align:center;font-size:13px;line-height:1.6;color:var(--white)}

/* testimonial */
.testimonial{left:0;top:1640px;width:1200px;height:355px;background:linear-gradient(135deg,#f3f3f3 0%,#e6e9ec 45%,#f5f5f5 100%)}
.avatar{left:562px;top:69px;width:76px;height:76px;border-radius:50%;background:#8f8f8f}
.quote{left:255px;top:168px;width:690px;text-align:center;font-style:italic;font-size:13px;line-height:1.86;color:#333}
.quote-name{left:0;top:252px;width:1200px;text-align:center;font-size:13px;color:#333}
.dots{left:574px;top:288px;display:flex;gap:6px}
.dots span{width:13px;height:13px;border-radius:50%;background:#b9b9b9}
.dots span.on{background:var(--coral)}

/* bottom */
.bottom{left:0;top:1995px;width:1200px;height:466px;background:var(--sand);overflow:hidden}
.col-title{font-size:30px;font-weight:400;color:#444;letter-spacing:.16em;line-height:1}
.col-sub{font-family:"Oswald","Arial Narrow",sans-serif;font-size:10px;letter-spacing:.2em;text-transform:uppercase;color:#444}
.col-text{font-size:13px;line-height:1.78;color:#444}
.skills-avatar{left:75px;top:225px;width:100px;height:100px;border-radius:50%;background:linear-gradient(180deg,#f6f1e8 0%,#f6f1e8 60%,#c66a36 60%,#c66a36 100%)}
.field{background:var(--sand-field);width:179px;height:29px;font-style:italic;font-size:12px;color:#999;padding:6px 10px}
.field.area{height:89px}
.btn-sm{display:block;border:1.5px solid #555;font-family:"Oswald","Arial Narrow",sans-serif;text-transform:uppercase;letter-spacing:.3em;font-size:12px;color:#333;text-align:center;line-height:26px;height:29px;text-decoration:none}
.article-title{font-family:"Oswald","Arial Narrow",sans-serif;font-size:14px;letter-spacing:.16em;text-transform:uppercase;color:var(--caramel)}

/* footer */
.footer{left:0;top:2461px;width:1200px;height:218px;background:var(--footer);color:#bbb;text-align:center}
.social{left:567px;top:18px;display:flex;gap:10px}
.social span{width:16px;height:16px;border-radius:50%;border:1.5px solid #ddd}
.foot-phone{left:0;top:44px;width:1200px;display:flex;justify-content:center;align-items:center;gap:8px;color:var(--white);font-size:26px}
.foot-address{left:0;top:92px;width:1200px;font-size:12px;line-height:1.6;color:#aaa}
.foot-mail{left:0;top:136px;width:1200px;display:flex;justify-content:center;align-items:center;gap:8px;font-size:13px;color:var(--white)}
.foot-copy{left:0;top:176px;width:1200px;font-size:10px;color:#999}
</style>
</head>
<body>

<header class="hero abs">
  <svg class="abs" style="left:0;top:0" width="1200" height="625" viewBox="0 0 1200 625" aria-hidden="true">
    <polygon points="348,0 890,0 1122,625 580,625" fill="#a6d6f7"/>
  </svg>
  <div class="topbar abs"></div>
  <div class="brand abs">pixelharbor</div>
  <nav class="nav abs">
    <a href="#" style="left:0">HOME</a>
    <a href="#" style="left:95px">ABOUT</a>
    <a href="#" style="left:197px">WORK</a>
    <a href="#" style="left:290px">BLOG</a>
    <a href="#" style="left:379px">CONTACT</a>
  </nav>
  <div class="phone abs">
    <svg width="18" height="18" viewBox="0 0 24 24" aria-hidden="true"><circle cx="12" cy="12" r="10.5" fill="none" stroke="#fff" stroke-width="2"/><path d="M8.5 7.2l1.7-.4 1 2.5-1.1 1a6.5 6.5 0 003.6 3.6l1-1.1 2.5 1-.4 1.7c-4.2.5-8.8-4.1-8.3-8.3z" fill="#fff"/></svg>
    415.555.0176
  </div>
  <div class="hero-kicker abs display">A perfect mix of</div>
  <div class="hero-title abs display">Web Wizardry</div>
  <div class="hero-title2 abs display">&amp; Creativity</div>
  <p class="hero-copy abs">A web developer is a programmer who specializes in, or is specifically engaged in, the development of web applications, or distributed network apps that are run over HTTP from a web server to a web browser.</p>
  <div class="hero-art abs" role="img" aria-label="Illustration of a developer working at a laptop on a wooden desk, with a wall clock and a framed landscape behind"></div>
</header>

<section class="services abs">
  <h2 class="section-title display abs" style="left:75px;top:120px">What I Do</h2>
  <div class="section-sub abs" style="left:76px;top:166px">Professional capabilities</div>
  <div class="services-art abs" role="img" aria-label="Illustration of a desktop monitor, keyboard and notepad with pencil seen from above"></div>

  <div class="service abs" style="left:527px;top:122px">
    <h3>Front/Back End</h3><h4>Development</h4>
    <p>Apple pie toffee tiramisu bonbon. Bonbon chocolate bar cupcake candy canes. Tart oat cake chocolate bar chocolate cake toffee cake wafer.</p>
  </div>
  <div class="service abs" style="left:888px;top:122px">
    <h3>E-Commerce</h3><h4>Development</h4>
    <p>Apple pie toffee tiramisu bonbon. Bonbon chocolate bar cupcake candy canes. Tart oat cake chocolate bar chocolate cake toffee cake wafer.</p>
  </div>
  <div class="service abs" style="left:527px;top:334px">
    <h3>User Interface</h3><h4>Design</h4>
    <p>Biscuit cake cotton candy brownie bonbon donut. Pudding toffee chocolate bar muffin candy drops cupcake toffee roll topping.</p>
  </div>
  <div class="service abs" style="left:888px;top:334px">
    <h3>Mobile App</h3><h4>Development</h4>
    <p>Biscuit cake cotton candy brownie bonbon donut. Pudding toffee chocolate bar muffin candy drops cupcake toffee roll topping.</p>
  </div>
  <a class="btn abs" style="left:527px;top:538px;width:241px" href="#">View all services</a>
</section>

<section class="work abs">
  <div class="tile abs" style="left:0;top:0;background:linear-gradient(135deg,#6b6b6b,#d9d9d9)" role="img" aria-label="Photo of hands holding a tablet beside a coffee cup"></div>
  <div class="tile abs" style="left:268px;top:0;background:linear-gradient(135deg,#8a8f95,#cfd6de)" role="img" aria-label="Photo of a person typing on a laptop"></div>
  <div class="tile abs" style="left:536px;top:0;background:linear-gradient(135deg,#bfc3c8,#e8e8e8)" role="img" aria-label="Photo of a notebook, phone and keyboard on a desk"></div>
  <div class="tile abs" style="left:0;top:179px;background:linear-gradient(135deg,#9a9a9a,#ececec)" role="img" aria-label="Photo of a laptop with headphones"></div>
  <div class="tile abs" style="left:268px;top:179px;background:linear-gradient(135deg,#7f7f7f,#dedede)" role="img" aria-label="Photo of a tablet, coffee pot and cup on a white table"></div>
  <div class="tile abs" style="left:536px;top:179px;background:linear-gradient(135deg,#d0d4d8,#5f6166)" role="img" aria-label="Photo of hands typing on a white keyboard"></div>
  <div class="work-panel abs">
    <svg class="abs" style="left:0;top:0" width="396" height="358" viewBox="0 0 396 358" aria-hidden="true"><polygon points="270,0 396,0 396,358 150,358" fill="#ee7a62"/></svg>
    <h2 class="display">My Work</h2>
    <h3>RECENT PROJECTS</h3>
    <p>Topping donut sesame snaps. Jelly beans soufflé halvah dessert sweet.</p>
  </div>
</section>

<section class="testimonial abs">
  <div class="avatar abs" role="img" aria-label="Portrait of the client giving the testimonial"></div>
  <p class="quote abs">Working with Pixelharbor was better than expected and we had really high expectations. He is an incredibly talented developer but what really makes him stand out is his work ethic and steady approach. Time after time, and without us asking, he added enhancements and improvements that resulted in a better end product for us.</p>
  <div class="quote-name abs">Dana K, OR</div>
  <div class="dots abs"><span></span><span class="on"></span><span></span></div>
</section>

<section class="bottom abs">
  <svg class="abs" style="left:0;top:0" width="1200" height="466" viewBox="0 0 1200 466" aria-hidden="true">
    <polygon points="290,0 690,0 860,466 460,466" fill="#f2e2bf"/>
  </svg>

  <h2 class="col-title display abs" style="left:75px;top:68px">Skills</h2>
  <div class="col-sub abs" style="left:75px;top:104px">Technologies I work with</div>
  <p class="col-text abs" style="left:75px;top:144px;width:260px">Sesame snaps topping toffee. Marzipan cookie jelly. Tart lemon drops donut cake.</p>
  <div class="skills-avatar abs" role="img" aria-label="Illustration of the developer at a laptop"></div>
  <p class="col-text abs" style="left:188px;top:218px;width:210px;font-size:12px">Korvo, Tesselkit<br>Garnet on Tracks<br>Quillscript, qLite, Vertex JS<br>Stylo, Markup, Tonic, Sextant Kit<br>Tuxbox, Heron, Ledger, Forge</p>
  <a class="btn-sm abs" style="left:75px;top:373px;width:114px" href="#">View bio</a>

  <h2 class="col-title display abs" style="left:434px;top:68px">Get in touch</h2>
  <div class="col-sub abs" style="left:434px;top:104px">Interested in working with me?</div>
  <div class="field abs" style="left:466px;top:152px">Name</div>
  <div class="field abs" style="left:466px;top:202px">Email</div>
  <div class="field area abs" style="left:466px;top:252px">What is this about?</div>
  <a class="btn-sm abs" style="left:466px;top:373px;width:116px" href="#">Send</a>

  <h2 class="col-title display abs" style="left:886px;top:68px">Articles</h2>
  <div class="col-sub abs" style="left:886px;top:104px">Some of my thoughts</div>
  <div class="article-title abs" style="left:886px;top:150px">Chocolate bar lollipop</div>
  <p class="col-text abs" style="left:886px;top:188px;width:250px;font-size:12.5px">Caramels powder gummies jujubes. Topping fruitcake sweet donut. Cake bonbon jelly marshmallow wafer. Dragée cake toffee tart pudding soufflé dessert oat cake sesame snaps. Gingerbread liquorice candy drops caramels sweet roll muffin cheesecake. Sweet roll lemon drops marzipan danish.</p>
  <a class="btn-sm abs" style="left:886px;top:373px;width:116px" href="#">Read more</a>
</section>

<footer class="footer abs">
  <div class="social abs"><span></span><span></span><span></span></div>
  <div class="foot-phone abs">
    <svg width="22" height="22" viewBox="0 0 24 24" aria-hidden="true"><circle cx="12" cy="12" r="10.5" fill="none" stroke="#fff" stroke-width="2"/><path d="M8.5 7.2l1.7-.4 1 2.5-1.1 1a6.5 6.5 0 003.6 3.6l1-1.1 2.5 1-.4 1.7c-4.2.5-8.8-4.1-8.3-8.3z" fill="#fff"/></svg>
    415.555.0176
  </div>
  <div class="foot-address abs">52 Lantern Row, Suite 8,<br>Maple Cove, OR 97031</div>
  <div class="foot-mail abs">
    <svg width="16" height="12" viewBox="0 0 16 12" aria-hidden="true"><rect x=".75" y=".75" width="14.5" height="10.5" fill="none" stroke="#fff" stroke-width="1.5"/><path d="M1 1l7 6 7-6" fill="none" stroke="#fff" stroke-width="1.5"/></svg>
    hello@pixelharbor.example
  </div>
  <div class="foot-copy abs">© 2016, All Rights Reserved</div>
</footer>

</body>
</html>
```